Verdalune Anti-Age Mask sticker design for brochure

We need a sticker go next or over our mother company logo and design info on the back of the brochure.
We develop, manufacture and market organic professional patch form skin solutions.

Feel free to explore and give us something we can use, for a near future change of look, that we are looking for, in order to work the US market
The Local company is :
Bortivex LLC
87 SW Ninth St. 4 Floor
Miami, FL 33175

Reason: Due to the few proposal i have decided to extend the submission deadline.. thank you...

Target Market(s)

estheticians , spa managers and workers, general public

Industry/Entity Type

It Company

Requirements
Must have
• Logo or similarity

```html
<!DOCTYPE html>
<html lang="en">
<head>
<meta charset="utf-8">
<title>Bortivex Sticker</title>
<link rel="stylesheet" href="https://fonts.googleapis.com/css2?family=Didact+Gothic&family=Questrial&display=swap">
<style>
  :root {
    --paper: #ffffff;
    --stone: #76736a;
    --ink: #76736a;
    --mist: #d0e3e3;
  }
  html, body {
    margin: 0;
    padding: 0;
    overflow: hidden;
    background: var(--paper);
  }
  .canvas {
    position: relative;
    width: 1200px;
    height: 843px;
    background: var(--paper);
    overflow: hidden;
  }
  .sticker-frame {
    position: absolute;
    left: 157px;
    top: 168px;
    width: 907px;
    height: 429px;
    border-radius: 44px;
    background: var(--stone);
  }
  .sticker-face {
    position: absolute;
    left: 2px;
    right: 2px;
    top: 15px;
    bottom: 15px;
    border-radius: 42px;
    background: var(--paper);
  }
  .brand-dot {
    position: absolute;
    left: 188px;
    top: 338px;
    width: 156px;
    height: 156px;
    border-radius: 50%;
    background: var(--mist);
  }
  .sticker-content {
    position: absolute;
    left: 326px;
    width: 730px;
    top: 368px;
    text-align: center;
    color: var(--ink);
  }
  .brand-name {
    margin: 0 -0.7em 0 0;
    font-family: "Questrial", sans-serif;
    font-weight: 400;
    font-size: 80px;
    line-height: 1;
    letter-spacing: 0.7em;
  }
  .address {
    margin: 2px 0 0;
    font-family: "Didact Gothic", sans-serif;
    font-style: normal;
    font-size: 48px;
    line-height: 56px;
    letter-spacing: 0.01em;
  }
</style>
</head>
<body>
  <div class="canvas">
    <div class="sticker-frame">
      <div class="sticker-face"></div>
    </div>
    <div class="brand-dot"></div>
    <div class="sticker-content">
      <p class="brand-name">Bortivex</p>
      <address class="address">87 SW Ninth St. 4 Floor, Miami<br>FL 33175</address>
    </div>
  </div>
</body>
</html>
```